Notepads for Marketing pieces-BOLD design

Looking for notepads for marketing pieces with logo, phone number, and website. Maybe something faded in background. Looking for bold and different

```html
<!DOCTYPE html>
<html lang="en">
<head>
<meta charset="UTF-8">
<title>Vitalline Care Notepad</title>
<link href="https://fonts.googleapis.com/css2?family=Poppins:wght@400;500;700&display=swap" rel="stylesheet">
<style>
  :root {
    --backdrop: #e6e6e6;
    --paper: #ffffff;
    --ink: #111111;
    --brand-red: #e21f26;
    --rule: #d3d3d3;
  }
  * { margin: 0; padding: 0; box-sizing: border-box; }
  html, body {
    width: 1154px;
    height: 1200px;
    overflow: hidden;
    background: var(--backdrop);
    font-family: "Poppins", sans-serif;
    color: var(--ink);
  }
  .notepad {
    position: absolute;
    left: 167px;
    top: 20px;
    width: 820px;
    height: 1160px;
    background: linear-gradient(180deg, #ffffff 0%, #fafafa 100%);
    border-bottom: 3px solid var(--brand-red);
    box-shadow: 0 6px 22px rgba(0,0,0,0.18);
  }
  .masthead {
    position: absolute;
    top: 92px;
    left: 0;
    width: 100%;
    text-align: center;
  }
  .brand-name {
    display: block;
    font-weight: 700;
    font-size: 40px;
    line-height: 1;
    letter-spacing: 2px;
    color: var(--brand-red);
    margin-left: 28px;
  }
  .service-list {
    display: block;
    margin-top: 10px;
    margin-left: 28px;
    font-weight: 500;
    font-size: 12px;
    color: var(--ink);
  }
  .writing-lines {
    position: absolute;
    left: 44px;
    top: 191px;
    width: 731px;
    height: 798px;
    background: repeating-linear-gradient(
      180deg,
      var(--rule) 0px,
      var(--rule) 1px,
      transparent 1px,
      transparent 34.65px
    );
  }
  .contact-row {
    position: absolute;
    top: 1034px;
    left: 0;
    width: 100%;
    display: flex;
    justify-content: center;
    align-items: center;
    font-size: 17px;
  }
  .contact-item {
    display: flex;
    align-items: center;
    gap: 14px;
  }
  .contact-item svg { width: 16px; height: 16px; fill: var(--brand-red); }
  .contact-divider {
    width: 1px;
    height: 40px;
    background: var(--brand-red);
    margin: 0 26px;
  }
  .tagline {
    position: absolute;
    top: 1093px;
    left: 0;
    width: 100%;
    text-align: center;
    font-size: 15.5px;
    font-weight: 500;
    letter-spacing: 0.5px;
  }
  .tagline .accent { color: var(--brand-red); }
</style>
</head>
<body>
  <main class="notepad">
    <header class="masthead">
      <span class="brand-name">VITALLINE CARE</span>
      <span class="service-list">Home Health | Medical Staffing | Outpatien Therapy</span>
    </header>

    <div class="writing-lines" aria-hidden="true"></div>

    <footer>
      <div class="contact-row">
        <div class="contact-item">
          <svg viewBox="0 0 24 24" aria-hidden="true">
            <path d="M3 9c0-3 4-5 9-5s9 2 9 5v2h-5V9c-1-1-7-1-8 0v2H3z"/>
            <path d="M6 12h12l2 8H4z"/>
          </svg>
          <span class="contact-phone">555.201.0148</span>
        </div>
        <div class="contact-divider"></div>
        <div class="contact-item">
          <svg viewBox="0 0 24 24" aria-hidden="true">
            <circle cx="12" cy="12" r="10"/>
            <path d="M7 8c2 0 3 1 3 3s-2 2-2 4 1 3 0 4c-2-1-4-4-4-7 0-2 1-4 3-4zM14 5c2 1 3 2 2 4s-3 1-3 3 2 2 3 1 2 1 1 3-3 3-4 2" fill="#ffffff"/>
          </svg>
          <span class="contact-web">www.vitallinecare.org</span>
        </div>
      </div>
      <p class="tagline">ONE MISSION, ONE <span class="accent">PRIORITY</span></p>
    </footer>
  </main>
</body>
</html>
```